Young Architect Bussiness Card

English is not my first language (spanish is).
Need a bussiness card design for my best friend who is about to graduate from college, Licentiate degree in architecture, so she needs business cards to start networking, currently she has no porfolio, web page or facebook. so she is relying on her cel phone and gmail, but should leave space for one of them (facebook)

Design for business card should be modern, maybe something with construction blue prints patern or 3D modelling.

Name: Mariela Fonseca Arrieta
Licentiate in Arquitecture
Cel: (506) XXX-4827
email: marielaXXX@correovela.com

Services, although im not sure if it has to be there or not:
Anteproyectos / Proposal design
Inspecciones / Site Inspections
Modelado 3D / 3D modelling
Planos Constructivos / Construction Blue Prints
Presupuestos / Budgets

Design should be in spanish

Contact Information for Business Card

Name: Mariela Fonseca, Arquitecto
Associtation code : XXXX
Phone: (506) XXXX-XXXX
Email: xxx@correovela.com
Facebook: xxxx

Requirements
Must have
• Design for business card should be modern, maybe something with construction blue prints patern or 3D modelling.
Nice to have
• Something like a transition from 2D to 3D.

```html
<!DOCTYPE html>
<html lang="es">
<head>
<meta charset="utf-8">
<title>Mariela Fonseca Arrieta — Tarjeta de presentación</title>
<link rel="stylesheet" href="https://fonts.googleapis.com/css2?family=Open+Sans:ital,wght@0,400;0,600;1,400&display=swap">
<style>
  :root {
    --page-bg: #e9e7e3;
    --card-white: #ffffff;
    --card-shade: #f1f2f3;
    --name-blue: #3a9fd2;
    --ink: #1d1d1d;
    --ink-soft: #555a5e;
    --back-ink: #3a3630;
    --photo-light: #dfe7ee;
    --photo-mid: #b9c9d6;
    --photo-yellow: #f2c21b;
  }
  * { box-sizing: border-box; margin: 0; padding: 0; }
  html, body { width: 1200px; height: 892px; overflow: hidden; }
  body {
    background: var(--page-bg);
    font-family: "Open Sans", Arial, sans-serif;
    position: relative;
  }
  .card {
    position: absolute;
    left: 320px;
    width: 560px;
    height: 320px;
    background: var(--card-white);
    box-shadow: 0 6px 18px rgba(0,0,0,0.18);
    overflow: hidden;
  }
  .card--front { top: 56px; }
  .card--back {
    top: 516px;
    display: flex;
    align-items: center;
    justify-content: center;
    background: linear-gradient(160deg, var(--card-white) 0%, var(--card-shade) 100%);
  }
  .front__photo {
    position: absolute;
    inset: 0 0 auto 0;
    height: 150px;
    background:
      radial-gradient(ellipse 90px 60px at 68% 40%, var(--photo-yellow) 0%, rgba(242,194,27,0) 100%),
      linear-gradient(120deg, var(--photo-light) 0%, var(--photo-mid) 70%, #8da0ae 100%);
  }
  .front__info {
    position: absolute;
    inset: 150px 0 0 0;
    background: linear-gradient(180deg, var(--card-white) 0%, var(--card-shade) 100%);
  }
  .front__name {
    position: absolute;
    left: 22px;
    top: 10px;
    font-size: 30px;
    font-weight: 400;
    color: var(--name-blue);
    letter-spacing: 0.2px;
  }
  .front__title {
    position: absolute;
    left: 24px;
    top: 54px;
    font-size: 15px;
    font-style: italic;
    color: var(--ink-soft);
  }
  .front__contact {
    position: absolute;
    right: 22px;
    bottom: 14px;
    list-style: none;
    text-align: right;
    font-size: 16px;
    line-height: 23px;
    color: var(--ink);
  }
  .contact__item { display: flex; justify-content: flex-end; align-items: center; gap: 8px; }
  .contact__icon { width: 13px; height: 13px; flex: none; }
  .contact__spacer { width: 13px; flex: none; }
  .back__name {
    font-size: 34px;
    font-weight: 400;
    color: var(--back-ink);
    letter-spacing: 0.5px;
  }
</style>
</head>
<body>
  <section class="card card--front">
    <div class="front__photo" role="img" aria-label="Fotografía de casco amarillo, nivel, cinta métrica y planos enrollados sobre planos arquitectónicos"></div>
    <div class="front__info">
      <h1 class="front__name">Mariela Fonseca Arrieta</h1>
      <p class="front__title">Licentiate in Arquitecture</p>
      <ul class="front__contact">
        <li class="contact__item">(506) XXX-4827
          <svg class="contact__icon" viewBox="0 0 16 16" aria-hidden="true"><path d="M2 5c0-2 2-3 6-3s6 1 6 3v1h-3V4.5H5V6H2z M4 7h8l2 7H2z" fill="#1d1d1d"/><circle cx="8" cy="10.5" r="2" fill="#fff"/></svg>
        </li>
        <li class="contact__item">marielaXXX@correovela.com
          <svg class="contact__icon" viewBox="0 0 16 16" aria-hidden="true"><rect x="1" y="3" width="14" height="10" fill="#1d1d1d"/><path d="M1.5 3.5 8 9l6.5-5.5" fill="none" stroke="#fff" stroke-width="1.2"/></svg>
        </li>
        <li class="contact__item">Associtation code : XXXX <span class="contact__spacer"></span></li>
        <li class="contact__item">Facebook: xxxx <span class="contact__spacer"></span></li>
      </ul>
    </div>
  </section>

  <section class="card card--back">
    <h2 class="back__name">Mariela Fonseca Arrieta</h2>
  </section>
</body>
</html>
```